Komira online ordering platform looking for a great web design

Komira - from the Vietnamese words Lộc Vân meaning financial success.
Background
Komira is an online ordering platform for small retail businesses (corner stores). The idea is that small retailers will use the website to order their supplies. From this we will utilise the group buying to get better deals for them that they could not achieve individually.
We are looking for a simple but stylish design for our ordering page. The layout needs to be efficient, logical and self explanatory.
Products to be sold on the site are FMCG (fast moving consumer goods). Potential to be 000's of items.
Considerations
- end users are not technologically adept.
- Users are generally older so small print will not be well received.
- Use of touch screen monitors to select/change items so spacing in design is vital.
- Logical display of category and sub-categories.
- Easy selection of products to order as well as modification of quantity.
- Shopping cart with easy change of item quantity.
- List of items for ordering can be paginated.
- Items listed will have image for easy identification.
- Search box
- Format should be in psd (photoshop) or complete html/css
- All this information needs to be displayed on the one page.
Product information to contain the following:
- Image
- Price
- Product name
- Size
Area for prominent display of specials without crowding the product information.

```html
<!DOCTYPE html>
<html lang="en">
<head>
<meta charset="utf-8">
<title>Komira – Online Store</title>
<link rel="stylesheet" href="https://fonts.googleapis.com/css2?family=Roboto:wght@300;400;500;700&display=swap">
<style>
:root{
  --red:#b50d0d;
  --red-dark:#8f0707;
  --ink:#333;
  --muted:#555;
  --panel:#2b2b2b;
  --blue:#1560d6;
  --orange:#e8601c;
  --page-bg:#ececec;
  --white:#fff;
}
*{box-sizing:border-box;margin:0;padding:0}
html,body{width:894px;height:1200px;overflow:hidden}
body{font-family:"Roboto",Arial,sans-serif;color:var(--ink);background:var(--page-bg);position:relative;font-size:9px}
a{color:inherit;text-decoration:none}
.abs{position:absolute}

/* top bar */
.topbar{left:0;top:0;width:894px;height:22px;background:linear-gradient(var(--red),var(--red-dark));color:var(--white)}
.topbar .welcome{left:129px;top:5px;font-size:9px;color:var(--white)}
.social{display:flex;gap:6px}
.social span{width:11px;height:11px;border-radius:50%;background:var(--white);display:block}
.topbar .social{left:684px;top:5px}

.sheet{left:106px;top:22px;width:683px;height:1088px;background:var(--white)}

/* header */
.logo{background:#2e2e2e;color:var(--white);font-size:31px;font-weight:400;line-height:38px;padding:0 4px;height:38px;letter-spacing:.5px}
.currency-label{left:490px;top:43px;font-size:9px;color:var(--muted)}
.select{background:var(--white);border:1px solid #bbb;font-size:9px;color:#444;padding-left:7px;display:flex;align-items:center}
.select::after{content:"";position:absolute;right:5px;top:50%;margin-top:-2px;border:3.5px solid transparent;border-top-color:#333}
.currency{left:541px;top:37px;width:72px;height:20px;background:#4a4a4a;color:var(--white);border:none}
.currency::after{border-top-color:var(--white)}
.cart{left:628px;top:37px;width:138px;height:39px;background:#222;color:var(--white)}
.cart .icon{left:0;top:0;width:39px;height:39px;background:var(--blue)}
.cart .t1{left:48px;top:7px;font-size:11px}
.cart .t2{left:48px;top:22px;font-size:9px;color:#999}

/* nav */
.nav{left:128px;top:90px;width:638px;height:36px;background:var(--red);display:flex;align-items:center}
.nav a{color:var(--white);font-size:14px;padding:0 12px 0 13px;border-right:1px solid #d44}
.nav a:last-of-type{border:none}
.nav .search{left:484px;top:8px;width:146px;height:20px;background:#222}
.nav .search i{position:absolute;right:0;top:0;width:20px;height:20px;background:#ddd}

/* hero */
.hero{left:128px;top:126px;width:480px;height:256px;background:linear-gradient(90deg,#d8d8d8,#ececec 55%,#d2d2d2)}
.hero .kicker{left:34px;top:27px;font-size:13px;font-weight:300;color:#6f6f6f}
.hero .year{left:32px;top:40px;font-size:48px;font-weight:700;color:var(--white);letter-spacing:-1px}
.hero .lead{left:34px;top:100px;font-size:8.5px;color:#6f6f6f;line-height:14px;width:232px}
.hero .excl{left:34px;top:144px;font-size:14px;color:#555;display:flex;align-items:center;gap:7px}
.hero .excl b{background:#2e2e2e;color:var(--white);font-weight:400;font-size:23px;padding:0 4px;line-height:26px}
.btn-dark{background:#444;color:var(--white);font-size:10px;display:flex;align-items:center;justify-content:center}
.hero .shop{left:34px;top:184px;width:84px;height:26px;font-size:10.5px;font-weight:500}
.hero .photo{left:272px;top:0;width:152px;height:256px;background:linear-gradient(#9a8c7a,#c9b59a 60%,#a89276)}
.hero .next{left:446px;top:94px;width:32px;height:54px;background:rgba(120,120,120,.5)}

/* specials */
.promo{left:608px;width:158px;height:94px;background:linear-gradient(#9b9b9b,#c4c4c4)}
.promo .img{left:8px;top:12px;width:72px;height:70px;background:#6b5a47;border-radius:6px}
.promo .title{left:84px;top:16px;font-size:17px;font-weight:700;color:var(--white);line-height:16px}
.promo .sub{left:84px;top:49px;font-size:6.5px;color:var(--white);white-space:nowrap}
.promo .now{left:84px;top:60px;width:54px;height:18px;background:#333;color:var(--white);font-size:7.5px;display:flex;align-items:center;justify-content:center}
.more{left:608px;top:316px;width:158px;height:66px;background:#f1f1f1}
.more p{position:absolute;left:13px;top:16px;font-size:13px;color:#666;font-weight:300;line-height:16px}
.more i{position:absolute;left:128px;top:18px;width:20px;height:20px;border-radius:50%;border:3px solid #888}

/* categories */
.cats{left:128px;top:382px;width:480px;height:134px;background:linear-gradient(#333,#1e1e1e)}
.cats h2{position:absolute;left:18px;top:10px;font-size:15px;font-weight:400;color:var(--white)}
.input{background:var(--white);border:1px solid #bbb;font-size:9px;color:#444;padding-left:7px;display:flex;align-items:center}
.btn-blue{background:var(--blue);color:var(--white);font-size:9px;display:flex;align-items:center;justify-content:center}
.btn-red{background:var(--red);color:var(--white);font-size:9px;font-weight:500;display:flex;align-items:center;justify-content:center}
.cats .ql{left:412px;top:11px;color:var(--white);font-size:7.5px}
.catcol{list-style:none;color:#e2e2e2;font-size:8.8px}
.catcol li{height:14px;position:relative;padding-left:15px;white-space:nowrap}
.catcol li.main::before{content:"";position:absolute;left:0;top:1px;width:9px;height:9px;border-radius:50%;background:var(--orange)}
.catcol li.sub::before{content:"";position:absolute;left:4px;top:3px;border:3px solid transparent;border-left-color:var(--orange)}

/* trolley */
.trolley{left:608px;top:382px;width:158px;height:134px;background:var(--white)}
.trolley h3{position:absolute;left:6px;top:6px;font-size:14px;font-weight:700}
.trolley .total{right:8px;top:4px;font-size:16px;font-weight:700;color:var(--blue)}
.lbl{font-size:9px;color:var(--muted);white-space:nowrap}
.btn-light{background:#f3f3f3;border:1px solid #bbb;font-size:8.5px;color:#333;display:flex;align-items:center;justify-content:center}

/* pager */
.pg{width:18px;height:18px;background:#555;color:var(--white);font-size:9px;display:flex;align-items:center;justify-content:center;font-weight:700}
.pg.on{background:var(--blue)}
.pg.arrow{background:var(--white);border:1px solid #aaa;color:#555}
.sortbar{left:128px;top:556px;width:641px;height:26px;background:#eee}

/* product cards */
.grid{left:128px;top:589px;display:grid;grid-template-columns:repeat(5,118px);column-gap:13px;row-gap:11.6px}
.card{position:relative;width:118px;height:118px;border:1px solid #cfcfcf;box-shadow:0 0 0 2px #f2f2f2 inset;background:var(--white)}
.card .img{left:6px;top:10px;width:42px;height:46px;background:linear-gradient(135deg,#333,#6a7fa8);border-radius:3px}
.card .img.light{background:linear-gradient(135deg,#eee,#bbb)}
.card .name{left:52px;top:10px;width:62px;font-size:9px;line-height:11px;font-weight:700;color:#8c0d0d}
.card .size{left:52px;top:34px;font-size:8.5px;color:#444}
.card .det{left:52px;top:46px;font-size:8.5px;color:#555;text-decoration:underline}
.card .price{right:10px;top:62px;font-size:14px;font-weight:700}
.card .q{left:6px;top:94px;font-size:8.5px;color:#555}
.card .qi{left:24px;top:89px;width:28px;height:20px;border:1px solid #bbb}
.card .pc{left:55px;top:94px;font-size:8.5px;color:#555}
.card .add{left:70px;top:89px;width:40px;height:20px;font-size:9.5px}

/* footer */
.footer{left:0;top:1110px;width:894px;height:90px;background:linear-gradient(var(--red),var(--red-dark))}
.footer nav{position:absolute;left:142px;top:21px;display:flex;gap:9px}
.footer nav a{color:var(--white);font-size:9px}
.footer .copy{left:142px;top:40px;color:var(--white);font-size:9px}
.footer .social{left:558px;top:33px}
.footer .logo{left:664px;top:20px}
</style>
</head>
<body>

<header class="abs topbar">
  <div class="abs welcome">Welcome visitor you can &nbsp;&nbsp; Create an account &nbsp;or&nbsp; Log in</div>
  <div class="abs social"><span></span><span></span><span></span><span></span><span></span></div>
</header>

<main class="abs sheet"></main>

<div class="abs logo" style="left:126px;top:36px">Komira</div>
<div class="abs currency-label">Currency</div>
<div class="abs select currency">US Dollar $</div>
<div class="abs cart">
  <div class="abs icon">
    <svg width="39" height="39" viewBox="0 0 39 39"><circle cx="11" cy="17" r="7" fill="#fff"/><rect x="7" y="16" width="8" height="2" fill="#1560d6"/><path d="M19 12h3l3 11h9l2-8H23" stroke="#fff" stroke-width="1.6" fill="none"/><circle cx="26" cy="26" r="1.5" fill="#fff"/><circle cx="33" cy="26" r="1.5" fill="#fff"/></svg>
  </div>
  <div class="abs t1">SHOPPING CART</div>
  <div class="abs t2">in cart 1 items</div>
</div>

<nav class="abs nav">
  <a href="#">ONLINE STORE</a><a href="#">ABOUT US</a><a href="#">DELIVERY</a><a href="#">FAQS</a><a href="#">CONTACTS</a>
  <div class="abs search"><i><svg width="20" height="20" viewBox="0 0 20 20"><circle cx="9" cy="9" r="4" stroke="#333" stroke-width="1.7" fill="none"/><path d="M12 12l3.5 3.5" stroke="#333" stroke-width="2"/></svg></i></div>
</nav>

<section class="abs hero">
  <div class="abs kicker">WOMEN'S COLLECTION</div>
  <div class="abs year">2013</div>
  <p class="abs lead">DONEC VITAE DIAM UT PURUS LUCTUS FACILIS. NULL AT LECTUS NON EROS TRISTIQUE ULTRICE.</p>
  <div class="abs excl">exclusive at <b>Komira</b></div>
  <div class="abs btn-dark shop">SHOP NOW</div>
  <div class="abs photo" role="img" aria-label="Model wearing a beige winter coat"></div>
  <div class="abs next"><svg width="32" height="54" viewBox="0 0 32 54"><path d="M13 19l8 8-8 8" stroke="#fff" stroke-width="1.5" fill="none"/></svg></div>
</section>

<aside class="abs promo" style="top:126px">
  <div class="abs img" role="img" aria-label="Brown leather boot"></div>
  <div class="abs title">NORTH&amp;<br>PINE</div>
  <div class="abs sub">BRUSHED HIDE BOOTS</div>
  <div class="abs now">SHOP NOW</div>
</aside>
<aside class="abs promo" style="top:220px">
  <div class="abs img" role="img" aria-label="Blue canvas backpack" style="background:#3c4d6b"></div>
  <div class="abs title">NORTH&amp;<br>PINE</div>
  <div class="abs sub">MOUNTAIN BAG</div>
  <div class="abs now">SHOP NOW</div>
</aside>
<div class="abs more"><p>More From This<br>Category</p><i></i></div>

<section class="abs cats">
  <h2>CATEGORIES</h2>
  <div class="abs input" style="left:130px;top:7px;width:110px;height:18px">search keywords</div>
  <div class="abs select" style="left:244px;top:7px;width:106px;height:18px">All products</div>
  <div class="abs btn-blue" style="left:354px;top:7px;width:52px;height:18px">SEARCH</div>
  <div class="abs ql">quicklist / search</div>
  <ul class="abs catcol" style="left:14px;top:42px">
    <li class="main">Accessories</li><li class="main">Home Phones</li><li class="sub">Lorem ipsum dolor</li><li class="sub">sit amet,</li><li class="sub">consectetuer</li><li class="sub">adipiscing elit, sed</li>
  </ul>
  <ul class="abs catcol" style="left:120px;top:42px">
    <li class="main">Cameras &amp; Camcorders</li><li class="main">MP3 &amp; Audio</li><li class="main">Cell Phones</li><li class="main">TVs &amp; Home Theater</li><li class="main">Photo Frames</li><li class="main">Computers &amp; Tablets</li>
  </ul>
  <ul class="abs catcol" style="left:238px;top:42px">
    <li class="main">GPS &amp; Navigation</li><li class="main">Car Audio</li><li class="main">EReaders</li><li class="sub" style="margin-top:3px">Lorem ipsum dolor</li><li class="sub">sit amet,</li><li class="sub">consectetuer</li>
  </ul>
  <ul class="abs catcol" style="left:350px;top:40px">
    <li class="main">Tablets / Phones</li><li class="sub">Lorem ipsum dolor</li><li class="sub">sit amet,</li><li class="sub">consectetuer</li><li class="sub">adipiscing elit, sed</li>
  </ul>
  <div class="abs btn-blue" style="left:352px;top:110px;width:106px;height:19px">More categories &nbsp;<b style="font-size:12px">+</b></div>
</section>

<section class="abs trolley">
  <h3>TROLLEY</h3>
  <div class="abs total">$6.59</div>
  <div class="abs lbl" style="left:6px;top:23px">(1 items)</div>
  <div class="abs input" style="left:6px;top:37px;width:52px;height:19px">product id</div>
  <div class="abs lbl" style="left:62px;top:42px">Qty.</div>
  <div class="abs input" style="left:80px;top:37px;width:24px;height:19px">3</div>
  <div class="abs btn-blue" style="left:108px;top:37px;width:44px;height:19px">Remove</div>
  <div class="abs btn-red" style="left:6px;top:61px;width:146px;height:24px;font-size:12px;font-weight:400;justify-content:flex-start;padding-left:10px">Checkout
    <svg class="abs" style="right:5px;top:4px" width="16" height="16" viewBox="0 0 16 16"><circle cx="8" cy="8" r="6.5" stroke="#fff" stroke-width="1.2" fill="none"/><path d="M6.5 5l3 3-3 3" stroke="#fff" stroke-width="1.2" fill="none"/></svg></div>
  <div class="abs lbl" style="left:6px;top:94px">sort by</div>
  <div class="abs select" style="left:72px;top:89px;width:80px;height:18px">recently added</div>
  <div class="abs btn-dark" style="left:6px;top:111px;width:62px;height:19px;font-size:8.5px">Clear Trolley</div>
  <div class="abs btn-light" style="left:88px;top:111px;width:64px;height:19px">Save Trolley</div>
</section>

<div class="abs lbl" style="left:129px;top:531px">Showing <b>1-20</b> of <b>330</b> items</div>
<div class="abs" style="left:250px;top:527px;display:flex;align-items:center">
  <div class="pg arrow">«</div>
  <div style="display:flex;gap:6px;margin-left:10px">
    <div class="pg on">1</div><div class="pg">2</div><div class="pg">3</div><div class="pg">4</div><div class="pg">5</div><div class="pg">6</div><div class="pg">7</div><div class="pg">8</div><div class="pg">9</div>
  </div>
  <span style="font-size:9px;margin:0 3px 0 2px">....</span>
  <div class="pg">19</div>
  <div class="pg arrow" style="margin-left:12px">»</div>
</div>
<div class="abs lbl" style="left:620px;top:531px;font-weight:700">show:</div>
<div class="abs select" style="left:650px;top:527px;width:42px;height:18px">20</div>
<div class="abs lbl" style="left:698px;top:531px">items per page</div>

<div class="abs sortbar">
  <div class="abs lbl" style="left:8px;top:8px">sort by:</div>
  <div class="abs select" style="left:46px;top:4px;width:128px;height:18px">category</div>
  <div class="abs lbl" style="left:462px;top:8px"><b>view:</b> &nbsp; shelf / list</div>
  <div class="abs lbl" style="left:547px;top:8px;font-weight:700">display images:</div>
  <div class="abs" style="left:619px;top:7px;width:11px;height:11px;border:1px solid #999;background:#fff">
    <svg width="11" height="11" viewBox="0 0 11 11" style="display:block"><path d="M2 5.5l2.2 2.2 4.5-5.5" stroke="#1560d6" stroke-width="1.5" fill="none"/></svg></div>
</div>

<div class="abs grid">
  <article class="card"><div class="abs img" role="img" aria-label="Tablet with keyboard"></div><div class="abs name">Aero Mouse Pro</div><div class="abs size">Size: 10 in</div><a class="abs det" href="#">details</a><div class="abs price">$6.59</div><div class="abs q">Qty</div><div class="abs qi"></div><div class="abs pc">pc</div><div class="abs btn-red add">Add</div></article>
  <article class="card"><div class="abs img" role="img" aria-label="Laptop"></div><div class="abs name">Aero Book Pro</div><div class="abs size">Size: 13 in</div><a class="abs det" href="#">details</a><div class="abs price">$6.59</div><div class="abs q">Qty</div><div class="abs qi"></div><div class="abs pc">pc</div><div class="abs btn-red add">Add</div></article>
  <article class="card"><div class="abs img" role="img" aria-label="Phone in box"></div><div class="abs name">Tabix</div><div class="abs size">Size: 5 in</div><a class="abs det" href="#">details</a><div class="abs price">$6.59</div><div class="abs q">Qty</div><div class="abs qi"></div><div class="abs pc">pc</div><div class="abs btn-red add">Add</div></article>
  <article class="card"><div class="abs img" role="img" aria-label="Tablet"></div><div class="abs name">Product name</div><div class="abs size">Size: 10 in</div><a class="abs det" href="#">details</a><div class="abs price">$6.59</div><div class="abs q">Qty</div><div class="abs qi"></div><div class="abs pc">pc</div><div class="abs btn-red add">Add</div></article>
  <article class="card"><div class="abs img light" role="img" aria-label="Stylus pens"></div><div class="abs name">Product name</div><div class="abs size">Size: 2 pack</div><a class="abs det" href="#">details</a><div class="abs price">$6.59</div><div class="abs q">Qty</div><div class="abs qi"></div><div class="abs pc">pc</div><div class="abs btn-red add">Add</div></article>

  <article class="card"><div class="abs img" role="img" aria-label="Tablet with keyboard"></div><div class="abs name">Aero Mouse Pro</div><div class="abs size">Size: 10 in</div><a class="abs det" href="#">details</a><div class="abs price">$6.59</div><div class="abs q">Qty</div><div class="abs qi"></div><div class="abs pc">pc</div><div class="abs btn-red add">Add</div></article>
  <article class="card"><div class="abs img" role="img" aria-label="Laptop"></div><div class="abs name">Aero Book Pro</div><div class="abs size">Size: 13 in</div><a class="abs det" href="#">details</a><div class="abs price">$6.59</div><div class="abs q">Qty</div><div class="abs qi"></div><div class="abs pc">pc</div><div class="abs btn-red add">Add</div></article>
  <article class="card"><div class="abs img" role="img" aria-label="Phone in box"></div><div class="abs name">Tabix</div><div class="abs size">Size: 5 in</div><a class="abs det" href="#">details</a><div class="abs price">$6.59</div><div class="abs q">Qty</div><div class="abs qi"></div><div class="abs pc">pc</div><div class="abs btn-red add">Add</div></article>
  <article class="card"><div class="abs img" role="img" aria-label="Tablet"></div><div class="abs name">Product name</div><div class="abs size">Size: 10 in</div><a class="abs det" href="#">details</a><div class="abs price">$6.59</div><div class="abs q">Qty</div><div class="abs qi"></div><div class="abs pc">pc</div><div class="abs btn-red add">Add</div></article>
  <article class="card"><div class="abs img light" role="img" aria-label="Stylus pens"></div><div class="abs name">Product name</div><div class="abs size">Size: 2 pack</div><a class="abs det" href="#">details</a><div class="abs price">$6.59</div><div class="abs q">Qty</div><div class="abs qi"></div><div class="abs pc">pc</div><div class="abs btn-red add">Add</div></article>

  <article class="card"><div class="abs img" role="img" aria-label="Tablet with keyboard"></div><div class="abs name">Aero Mouse Pro</div><div class="abs size">Size: 10 in</div><a class="abs det" href="#">details</a><div class="abs price">$6.59</div><div class="abs q">Qty</div><div class="abs qi"></div><div class="abs pc">pc</div><div class="abs btn-red add">Add</div></article>
  <article class="card"><div class="abs img" role="img" aria-label="Laptop"></div><div class="abs name">Aero Book Pro</div><div class="abs size">Size: 13 in</div><a class="abs det" href="#">details</a><div class="abs price">$6.59</div><div class="abs q">Qty</div><div class="abs qi"></div><div class="abs pc">pc</div><div class="abs btn-red add">Add</div></article>
  <article class="card"><div class="abs img" role="img" aria-label="Phone in box"></div><div class="abs name">Tabix</div><div class="abs size">Size: 5 in</div><a class="abs det" href="#">details</a><div class="abs price">$6.59</div><div class="abs q">Qty</div><div class="abs qi"></div><div class="abs pc">pc</div><div class="abs btn-red add">Add</div></article>
  <article class="card"><div class="abs img" role="img" aria-label="Tablet"></div><div class="abs name">Product name</div><div class="abs size">Size: 10 in</div><a class="abs det" href="#">details</a><div class="abs price">$6.59</div><div class="abs q">Qty</div><div class="abs qi"></div><div class="abs pc">pc</div><div class="abs btn-red add">Add</div></article>
  <article class="card"><div class="abs img light" role="img" aria-label="Stylus pens"></div><div class="abs name">Product name</div><div class="abs size">Size: 2 pack</div><a class="abs det" href="#">details</a><div class="abs price">$6.59</div><div class="abs q">Qty</div><div class="abs qi"></div><div class="abs pc">pc</div><div class="abs btn-red add">Add</div></article>

  <article class="card"><div class="abs img" role="img" aria-label="Tablet with keyboard"></div><div class="abs name">Aero Mouse Pro</div><div class="abs size">Size: 10 in</div><a class="abs det" href="#">details</a><div class="abs price">$6.59</div><div class="abs q">Qty</div><div class="abs qi"></div><div class="abs pc">pc</div><div class="abs btn-red add">Add</div></article>
  <article class="card"><div class="abs img" role="img" aria-label="Laptop"></div><div class="abs name">Aero Book Pro</div><div class="abs size">Size: 13 in</div><a class="abs det" href="#">details</a><div class="abs price">$6.59</div><div class="abs q">Qty</div><div class="abs qi"></div><div class="abs pc">pc</div><div class="abs btn-red add">Add</div></article>
  <article class="card"><div class="abs img" role="img" aria-label="Phone in box"></div><div class="abs name">Tabix</div><div class="abs size">Size: 5 in</div><a class="abs det" href="#">details</a><div class="abs price">$6.59</div><div class="abs q">Qty</div><div class="abs qi"></div><div class="abs pc">pc</div><div class="abs btn-red add">Add</div></article>
  <article class="card"><div class="abs img" role="img" aria-label="Tablet"></div><div class="abs name">Product name</div><div class="abs size">Size: 10 in</div><a class="abs det" href="#">details</a><div class="abs price">$6.59</div><div class="abs q">Qty</div><div class="abs qi"></div><div class="abs pc">pc</div><div class="abs btn-red add">Add</div></article>
  <article class="card"><div class="abs img light" role="img" aria-label="Stylus pens"></div><div class="abs name">Product name</div><div class="abs size">Size: 2 pack</div><a class="abs det" href="#">details</a><div class="abs price">$6.59</div><div class="abs q">Qty</div><div class="abs qi"></div><div class="abs pc">pc</div><div class="abs btn-red add">Add</div></article>
</div>

<footer class="abs footer">
  <nav><a href="#">Online</a><a href="#">Store</a><a href="#">About Us</a><a href="#">Delivery</a><a href="#">FAQs</a><a href="#">Contacts</a></nav>
  <div class="abs copy">Copyright © 2013 Komira. All Rights Reserved.</div>
  <div class="abs social"><span></span><span></span><span></span><span></span><span></span></div>
  <div class="abs logo">Komira</div>
</footer>

</body>
</html>
```